5-6 page Website Design- Rooted Stillness Program, including 2 videos

We need an elegantly simple and beautiful website for the Rooted Stillness Program (RSP), a 6-month program for founders and leaders of startups who want to shift from Actors to Authors in their leadership.
At a minimum, the website will include:
Home Page
Program Description--Why Actor to Author?
Program Timeline and Structure
Testimonials and Past Clients (this page will include a testimonials video and text)
Team
FAQs
I'd like to see two versions of The Home Page/Landing Page:
1. Just an image with the words
If your startup is growing rapidly,
we can help you do the same.
RSP: The ACTOR to AUTHOR Shift
2. A place for a video describing the program
No payment integration on the website. Just information.
Startup founders and senior leaders

```html
<!DOCTYPE html>
<html lang="en">
<head>
<meta charset="utf-8">
<title>Rooted Stillness Program – Website Design</title>
<link href="https://fonts.googleapis.com/css2?family=Montserrat:ital,wght@0,500;0,600;0,700;1,600;1,700&family=Roboto:wght@400;500;700&display=swap" rel="stylesheet">
<style>
:root{
  --board:#e4e6e9;
  --blue:#0d56a6;
  --blue-light:#2697dc;
  --blue-mid:#1c7fcc;
  --ink:#1f1f1f;
  --text:#6b6b6b;
  --white:#ffffff;
  --footer:#222326;
  --footer-text:#c9c9c9;
}
*{margin:0;padding:0;box-sizing:border-box}
html,body{width:690px;height:1200px;overflow:hidden;background:var(--board)}
.board{position:relative;width:1456px;height:2533px;transform:scale(.47390);transform-origin:0 0;background:var(--board);font-family:"Roboto",Arial,sans-serif;color:var(--ink)}
.a{position:absolute}
.page{position:absolute;left:85px;top:77px;width:602px;height:2378px;background:var(--white);overflow:hidden}
.logo{display:flex;align-items:center;gap:8px}
.logo-dot{width:30px;height:30px;border-radius:50%;background:var(--white)}
.logo-name{font-family:"Montserrat",sans-serif;font-weight:600;color:var(--white);font-size:9.5px;line-height:10px;text-transform:uppercase}
.logo.big .logo-dot{width:40px;height:40px}
.logo.big .logo-name{font-size:12.5px;line-height:12px}
.top-contact{font-size:7px;color:var(--white);display:flex;gap:14px}
.nav{display:flex;gap:12px;font-size:7px;font-weight:500;color:var(--white)}
.panel-photo{position:absolute}
.eyebrow{font-family:"Montserrat",sans-serif;font-weight:600;font-size:7.5px;text-transform:uppercase;color:var(--ink)}
.eyebrow.light{color:var(--white)}
.title{font-family:"Montserrat",sans-serif;font-weight:600;font-size:15px;color:var(--blue-mid);text-transform:uppercase}
.title.light{color:var(--white)}
.heading-bar{border-left:2px solid var(--blue);padding-left:10px}
.heading-bar.light{border-color:var(--white)}
.hero-title{font-family:"Montserrat",sans-serif;font-weight:600;font-size:18px;line-height:18px;color:var(--white);text-transform:uppercase}
.body{font-size:7px;line-height:13px;color:var(--text);text-align:justify}
.body.light{color:#e9ecf2}
.btn{display:inline-flex;align-items:center;gap:6px;background:var(--blue);color:var(--white);font-size:7px;font-weight:700;text-transform:uppercase;padding:0 8px;height:24px;border-radius:2px}
.btn-arrow{width:8px;height:8px;border-radius:50%;background:var(--white);position:relative}
.btn-arrow::after{content:"";position:absolute;left:3px;top:2px;border-left:3px solid var(--blue);border-top:2px solid transparent;border-bottom:2px solid transparent}
.dots{display:flex;gap:3px}
.dots i{width:5px;height:5px;border-radius:50%;background:var(--white);display:block}
.center{text-align:center}
.tl-line{position:absolute;width:3px;height:370px;background:#d6dbe1}
.tl-node{position:absolute;width:11px;height:11px;border-radius:50%;border:2px solid var(--blue-light);background:var(--white)}
.month{position:absolute;width:85px;height:24px;color:var(--white);font-family:"Montserrat",sans-serif;font-weight:600;font-size:8.5px;display:flex;align-items:center;justify-content:center}
.month.right{background:var(--blue-light);clip-path:polygon(6px 0,100% 0,100% 100%,6px 100%,6px 65%,0 50%,6px 35%)}
.month.left{background:var(--blue);clip-path:polygon(0 0,calc(100% - 6px) 0,calc(100% - 6px) 35%,100% 50%,calc(100% - 6px) 65%,calc(100% - 6px) 100%,0 100%)}
.weeks{position:absolute;list-style:none;font-size:6.3px;line-height:12px;color:var(--text)}
.weeks li{display:flex;gap:6px;align-items:center}
.weeks li::before{content:"";width:4px;height:4px;border-radius:50%;border:1.3px solid var(--blue-light)}
.weeks b{color:var(--blue-mid);font-weight:700;width:24px}
.stage{position:absolute;background:var(--white);box-shadow:0 1px 4px rgba(0,0,0,.12);font-family:"Montserrat",sans-serif;font-weight:600;font-size:8px;color:#444;height:19px;display:flex;align-items:center;justify-content:center}
.card{position:absolute;width:239px;height:131px;background:var(--white);border-radius:6px;padding:3px;display:flex;gap:14px}
.card-photo{width:96px;height:125px;border-radius:3px;background:linear-gradient(160deg,#dfe3e8,#9aa6b5 60%,#3d4a5c);position:relative;flex:none}
.play{position:absolute;width:14px;height:14px;border-radius:50%;background:var(--blue-light)}
.play::after{content:"";position:absolute;left:5px;top:3.5px;border-left:5px solid var(--white);border-top:3.5px solid transparent;border-bottom:3.5px solid transparent}
.card-brand{font-family:"Roboto",sans-serif;font-size:10px;color:#333;margin-top:14px}
.quote-mark{font-family:"Montserrat",sans-serif;font-weight:700;font-size:20px;line-height:16px;color:var(--blue-light);margin-top:4px}
.card-text{font-size:6.3px;line-height:10.5px;color:var(--text);font-style:italic;text-align:justify;margin-top:4px;width:116px}
.card-name{font-size:6.5px;font-weight:700;margin-top:8px}
.card-role{font-size:6.5px;color:var(--text)}
.arrow-nav{position:absolute;width:8px;height:8px;border-top:1.5px solid var(--white);border-right:1.5px solid var(--white)}
.member{position:absolute;width:150px;text-align:center}
.member-photo{width:114px;height:114px;margin:0 auto;border-radius:50%;background:linear-gradient(170deg,#e4e7eb,#b6bfca 55%,#45546a);border-top:3px solid var(--blue)}
.member-name{font-size:9.5px;font-weight:700;margin-top:12px}
.member-role{font-size:7px;color:var(--text);margin-top:3px}
.member-bio{font-size:6.5px;line-height:10.5px;color:var(--text);margin-top:5px}
.socials{display:flex;justify-content:center;gap:4px;margin-top:8px}
.socials i{width:13px;height:13px;border-radius:50%;background:var(--blue-light);display:block}
.footer{position:absolute;left:0;top:2197px;width:602px;height:181px;background:var(--footer)}
.f-col{position:absolute;top:15px;color:var(--footer-text)}
.f-head{font-size:7px;font-weight:700;color:var(--white);text-transform:uppercase;margin-bottom:12px}
.f-list{list-style:none;font-size:6.3px;line-height:15px}
.f-list li::before{content:"» ";color:var(--white)}
.f-contact{list-style:none;font-size:6.3px;line-height:17px}
.f-contact li{display:flex;gap:6px;align-items:center}
.f-contact li::before{content:"";width:5px;height:5px;background:var(--white);border-radius:50%}
.f-contact li.cont::before{background:transparent}
.f-divider{position:absolute;top:15px;width:1px;height:110px;background:#55575c}
.f-input{width:124px;height:20px;background:var(--white);font-size:6.3px;color:#777;display:flex;align-items:center;padding-left:7px;margin-top:8px}
.f-btn{display:inline-flex;align-items:center;height:20px;padding:0 12px;background:var(--blue);color:var(--white);font-size:6.5px;font-weight:700;margin-top:4px}
.f-social{width:17px;height:17px;border-radius:50%;border:1px solid var(--footer-text);display:block}
.panel{position:absolute;left:769px;width:602px;overflow:hidden}
.panel-text{font-family:"Montserrat",sans-serif;font-weight:600;color:var(--white);text-transform:uppercase;font-size:16.5px;line-height:23px;text-align:center}
.panel-tag{font-family:"Montserrat",sans-serif;font-weight:700;color:var(--white);font-size:24px;text-align:center}
.panel-quote{font-family:"Montserrat",sans-serif;font-weight:600;font-style:italic;color:var(--white);font-size:10.3px;line-height:17px;text-align:center}
.panel-body{font-size:6.4px;line-height:10.8px;color:#e6edf5;text-align:justify;text-align-last:center}
</style>
</head>
<body>
<div class="board">

  <!-- Website home page -->
  <div class="page">

    <!-- Hero -->
    <svg class="a" style="left:0;top:0" width="602" height="370" viewBox="0 0 602 370">
      <defs>
        <linearGradient id="lake" x1="0" y1="0" x2="0" y2="1">
          <stop offset="0" stop-color="#3e4c66"/>
          <stop offset=".3" stop-color="#62728f"/>
          <stop offset=".48" stop-color="#a7b2c3"/>
          <stop offset=".62" stop-color="#6f7f98"/>
          <stop offset=".85" stop-color="#3f4b5f"/>
          <stop offset="1" stop-color="#2a3342"/>
        </linearGradient>
      </defs>
      <path d="M0,0 L602,0 L602,268 Q301,416 0,268Z" fill="url(#lake)" role="img" aria-label="Lakeside jetty with a wooden bench at dusk, calm water and distant hills"/>
      <path d="M0,268 Q301,416 602,268 Q301,460 0,268Z" fill="#1868b8"/>
    </svg>
    <div class="a logo" style="left:58px;top:8px"><span class="logo-dot"></span><span class="logo-name">Rooted<br>Stillness<br>Program</span></div>
    <div class="a top-contact" style="left:310px;top:8px"><span>✉ hello@rootedstillness.org</span><span>|</span><span>☎ +1 555 014 2290</span></div>
    <div class="a nav" style="left:243px;top:31px"><span>Home</span><span>Program Description</span><span>Program Timeline</span><span>Testimonials</span><span>Team</span><span>FAQ</span><span>Contact</span></div>
    <div class="a eyebrow light" style="left:56px;top:111px">Welcome to</div>
    <div class="a hero-title" style="left:56px;top:130px">Rooted Stillness<br>Program</div>
    <div class="a" style="left:56px;top:175px;font-size:7px;line-height:11px;color:#fff;font-weight:500">Lorem ipsum dolor sit amet, consectetur adipiscing elit, sed<br>do eiusmod tempor incididunt ut labore</div>
    <div class="a btn" style="left:56px;top:206px">Get Started <span class="btn-arrow"></span></div>
    <div class="a dots" style="left:288px;top:258px"><i></i><i></i><i></i><i></i></div>

    <!-- Program description -->
    <div class="a" role="img" aria-label="Two women talking across a table in a bright office" style="left:54px;top:393px;width:212px;height:212px;border-radius:50%;background:linear-gradient(135deg,#dfe2e6 0%,#b9a99a 40%,#6f5d50 70%,#c7ccd2 100%)"></div>
    <svg class="a" style="left:40px;top:380px" width="250" height="250" viewBox="0 0 250 250">
      <path d="M125,7 A118,118 0 1 1 30,195" fill="none" stroke="#1c7fcc" stroke-width="6"/>
    </svg>
    <div class="a heading-bar" style="left:328px;top:410px"><div class="eyebrow">Introduction</div><div class="title" style="margin-top:3px">Program Description</div></div>
    <p class="a body" style="left:328px;top:446px;width:218px">Well thanks Clara, sounds pretty simple...but what about when I've got 11 back-to-back meetings, a board meeting to prepare for with investors who have sky-high expectations, 6 new hires to onboard and 16 more to find, and–not least–a product to improve for the customers we are trying to serve and retain–only to wake up, rinse (maybe) and repeat tomorrow?? (We didn't even mention the chat and email messages mounting in the background.) How could I possibly exit "busy anxiousness" and practice calm centeredness amidst this chaos?</p>
    <div class="a btn" style="left:328px;top:571px">Learn More <span class="btn-arrow"></span></div>

    <!-- Why choose us -->
    <svg class="a" style="left:0;top:628px" width="602" height="390" viewBox="0 0 602 390">
      <defs>
        <linearGradient id="dusk" x1="0" y1="0" x2="0" y2="1">
          <stop offset="0" stop-color="#5d6584"/>
          <stop offset=".45" stop-color="#8c7f8d"/>
          <stop offset=".6" stop-color="#b98a6e"/>
          <stop offset=".8" stop-color="#3e3a44"/>
          <stop offset="1" stop-color="#1f2027"/>
        </linearGradient>
      </defs>
      <path d="M20,88 Q301,-72 582,88 Q301,-30 20,88Z" fill="#2390d8"/>
      <path d="M0,300 Q301,461 602,300 Q301,415 0,300Z" fill="#1560b0"/>
      <path d="M0,92 Q301,-30 602,92 L602,300 Q301,415 0,300Z" fill="url(#dusk)" role="img" aria-label="Two hikers helping each other up a rock at sunset"/>
    </svg>
    <div class="a heading-bar light" style="left:56px;top:722px"><div class="eyebrow light">Why choose us</div><div class="title light" style="margin-top:3px">The Logic Behind the Structure</div></div>
    <div class="a" style="left:56px;top:757px;font-size:8px;font-weight:700;color:#fff">Why retreats? Immersion!</div>
    <p class="a body light" style="left:56px;top:773px;width:257px">The retreat environment creates an immersive experience, co-created by group. The sharp distinction from the fast pace of everyday startup life helps participants stand outside their everyday habits and evaluate which ones they want to change. Furthermore, just like in learning a language, immersion is the most powerful context for learning and ingraining new habits. Even so, we are wary of the format taken by many retreats/bootcamps which focus on just this one-off peak experience, neither sowing the seeds beforehand nor offering follow-up support for integrating the new insights and practices back in the regular world. Our workshops and coaching structure</p>
    <div class="a btn" style="left:56px;top:896px">Learn More <span class="btn-arrow"></span></div>

    <!-- Program timeline -->
    <div class="a" role="img" aria-label="Faint misty mountain landscape" style="left:0;top:1010px;width:602px;height:527px;background:linear-gradient(180deg,#ffffff 0%,#eef1f5 20%,#e6eaf0 60%,#f3f5f8 100%)"></div>
    <div class="a heading-bar" style="left:226px;top:1037px"><div class="eyebrow" style="padding-left:42px">Structure</div><div class="title" style="margin-top:3px">Program Timeline</div></div>
    <div class="a center" style="left:0;width:602px;top:1071px;font-size:8px;font-weight:500;color:#444">Everything will be virtual except the 2 retreats</div>
    <div class="stage" style="left:241px;top:1097px;width:120px">Leading Yourself</div>
    <div class="tl-line" style="left:299px;top:1128px"></div>

    <div class="tl-node" style="left:295px;top:1132px"></div>
    <div class="month right" style="left:333px;top:1126px">MONTH - 01</div>
    <ul class="weeks" style="left:140px;top:1129px"><li><b>Week 1</b>: Kickoff Orientation Workshop</li><li><b>Week 2</b>: 1on1 Exec Coaching Session</li><li><b>Week 3</b>: Workshop</li></ul>

    <div class="tl-node" style="left:295px;top:1188px"></div>
    <div class="month left" style="left:187px;top:1182px">MONTH - 02</div>
    <ul class="weeks" style="left:335px;top:1185px"><li><b>Week 1</b>: 1st Retreat ("Leading Yourself")</li><li><b>Week 2</b>: 1on1 Exec Coaching Session</li><li><b>Week 4</b>: Workshop</li></ul>

    <div class="tl-node" style="left:295px;top:1244px"></div>
    <div class="month right" style="left:333px;top:1238px">MONTH - 03</div>
    <ul class="weeks" style="left:140px;top:1241px"><li><b>Week 2</b>: 1on1 Exec Coaching Session</li><li><b>Week 4</b>: 1on1 Exec Coaching Session</li></ul>

    <div class="stage" style="left:213px;top:1291px;width:176px">Leading Relationships, Leading Others</div>

    <div class="tl-node" style="left:295px;top:1340px"></div>
    <div class="month left" style="left:187px;top:1334px">MONTH - 04</div>
    <ul class="weeks" style="left:335px;top:1340px"><li><b>Week 2</b>: 1on1 Exec Coaching Session</li></ul>

    <div class="tl-node" style="left:295px;top:1396px"></div>
    <div class="month right" style="left:333px;top:1390px">MONTH - 05</div>
    <ul class="weeks" style="left:140px;top:1393px"><li><b>Week 1</b>: 2nd Retreat</li><li><b>Week 2</b>: 1on1 Exec Coaching Session</li><li><b>Week 4</b>: Workshop</li></ul>

    <div class="tl-node" style="left:295px;top:1452px"></div>
    <div class="month left" style="left:187px;top:1446px">MONTH - 06</div>
    <ul class="weeks" style="left:335px;top:1449px"><li><b>Week 2</b>: 1on1 Exec Coaching Session</li><li><b>Week 4</b>: Concluding Workshop</li><li><b>Week 5</b>: Concluding 1on1 Exec Coaching Session</li></ul>

    <!-- Testimonials -->
    <div class="a" style="left:0;top:1537px;width:602px;height:246px;background:linear-gradient(90deg,#1f86d3,#2a9ce0)"></div>
    <div class="a heading-bar light" style="left:212px;top:1569px"><div class="eyebrow light" style="padding-left:50px">Testimonials</div><div class="title light" style="margin-top:3px">What Our Clients Say</div></div>
    <div class="arrow-nav" style="left:28px;top:1677px;transform:rotate(-135deg)"></div>
    <div class="arrow-nav" style="left:567px;top:1677px;transform:rotate(45deg)"></div>
    <div class="card" style="left:56px;top:1615px">
      <div class="card-photo" role="img" aria-label="Client portrait in a business suit"><span class="play" style="left:41px;top:55px"></span></div>
      <div><div class="card-brand">○ Northway</div><div class="quote-mark">“</div><p class="card-text">Lorem ipsum dolor sit consectetur adipiscing elit, sed do eiusm tempor incididunt ut labore et dolore magna aliqua. Ut enim ad minim</p><div class="card-name">SAM RIVERS</div><div class="card-role">Businessman</div></div>
    </div>
    <div class="card" style="left:307px;top:1615px">
      <div class="card-photo" role="img" aria-label="Client portrait in a business suit"><span class="play" style="left:41px;top:55px"></span></div>
      <div><div class="card-brand">○ Northway</div><div class="quote-mark">“</div><p class="card-text">Lorem ipsum dolor sit consectetur adipiscing elit, sed do eiusm tempor incididunt ut labore et dolore magna aliqua. Ut enim ad minim</p><div class="card-name">SAM RIVERS</div><div class="card-role">Businessman</div></div>
    </div>

    <!-- Team -->
    <div class="a heading-bar" style="left:239px;top:1826px"><div class="eyebrow" style="padding-left:23px">Our Partners</div><div class="title" style="margin-top:3px">Meet Our Team</div></div>
    <div class="member" style="left:53px;top:1866px"><div class="member-photo" role="img" aria-label="Team member portrait"></div><div class="member-name">Daniel Hartley</div><div class="member-role">Businessman</div><p class="member-bio">Sed ut perspiciatis unde omnis iste natus error sitvoluptatemaccusantiumdoloremqulaudanti um, totam rem aperiam</p><div class="socials"><i></i><i></i></div></div>
    <div class="member" style="left:226px;top:1866px"><div class="member-photo" role="img" aria-label="Team member portrait"></div><div class="member-name">Daniel Hartley</div><div class="member-role">Businessman</div><p class="member-bio">Sed ut perspiciatis unde omnis iste natus error sitvoluptatemaccusantiumdoloremqulaudanti um, totam rem aperiam</p><div class="socials"><i></i><i></i></div></div>
    <div class="member" style="left:400px;top:1866px"><div class="member-photo" role="img" aria-label="Team member portrait"></div><div class="member-name">Daniel Hartley</div><div class="member-role">Businessman</div><p class="member-bio">Sed ut perspiciatis unde omnis iste natus error sitvoluptatemaccusantiumdoloremqulaudanti um, totam rem aperiam</p><div class="socials"><i></i><i></i></div></div>

    <!-- Footer -->
    <svg class="a" style="left:0;top:2093px" width="602" height="106" viewBox="0 0 602 106">
      <path d="M0,105 Q301,-95 602,105 Q301,-20 0,105Z" fill="#1868b8"/>
    </svg>
    <div class="footer">
      <div class="f-col" style="left:56px"><div class="f-head">Quick Links</div><ul class="f-list"><li>Home</li><li>Program Description</li><li>Program Timeline</li><li>Logic Behind the Structure</li><li>Testimonials</li></ul></div>
      <div class="f-divider" style="left:155px"></div>
      <div class="f-col" style="left:177px"><div class="f-head">Other Links</div><ul class="f-list"><li>FAQ</li><li>Meet our Team</li><li>Terms &amp; Condition</li><li>Privacy Policy</li><li>Help Service</li></ul></div>
      <div class="f-divider" style="left:256px"></div>
      <div class="f-col" style="left:277px"><div class="f-head">Contact Us</div><ul class="f-contact"><li>18 Wattle Lane, Brookvale 4821</li><li class="cont">United States</li><li>info@rsp.org</li><li>+1 555 014 2290</li><li>+1 555 014 7731</li></ul></div>
      <div class="f-divider" style="left:395px"></div>
      <div class="f-col" style="left:422px"><div class="f-head">Newsletter</div><div style="font-size:6px;font-weight:700;color:#fff;line-height:10px">SUBSCRIBE TO OUR NEWSLETTER TO<br>STAY UP TO DATE ON NEWS AND</div><div class="f-input">Email Address</div><div class="f-btn">SUBSCRIBE</div></div>
      <div class="a" style="left:56px;top:139px;width:490px;height:1px;background:#55575c"></div>
      <div class="a" style="left:56px;top:155px;font-size:6.8px;color:var(--footer-text)">© 2022 Rooted Stillness Program. All Rights Reserved.</div>
      <div class="a" style="left:481px;top:151px;display:flex;gap:6px"><i class="f-social"></i><i class="f-social"></i><i class="f-social"></i></div>
    </div>
  </div>

  <!-- Landing version 1: image with words -->
  <div class="panel" style="top:77px;height:323px">
    <div class="panel-photo" role="img" aria-label="Sun setting behind mountains over a still lake, with a faint silhouette" style="inset:0;background:radial-gradient(ellipse at 45% 48%,#f2b276 0%,#c7806a 18%,#6e5d6f 45%,#3c3f52 75%,#2a2c38 100%)"></div>
    <div class="a logo big" style="left:236px;top:28px"><span class="logo-dot"></span><span class="logo-name">Rooted<br>Stillness<br>Program</span></div>
    <div class="a panel-text" style="left:0;width:602px;top:153px">If your startup is growing rapidly<br>we can help you do the same.</div>
    <div class="a panel-tag" style="left:0;width:602px;top:210px">RSP : The ACTOR to AUTHOR Shift</div>
  </div>

  <!-- Landing version 2: video -->
  <div class="panel" style="top:469px;height:344px">
    <div class="panel-photo" role="img" aria-label="Person standing on a rocky ridge above a blue mountain valley" style="inset:0;background:linear-gradient(180deg,#3f6f9e 0%,#4d7eab 35%,#3a6690 60%,#22415f 85%,#1a3149 100%)"></div>
    <div class="a logo big" style="left:236px;top:8px"><span class="logo-dot"></span><span class="logo-name">Rooted<br>Stillness<br>Program</span></div>
    <p class="a panel-quote" style="left:30px;width:542px;top:108px">“If you want to be busy and anxious practice busy anxiousness. If you want to be calm centered,<br>practice it. It’s as simple as that.”</p>
    <p class="a panel-body" style="left:56px;width:490px;top:155px">Well thanks Clara, sounds pretty simple...but what about when I've got 11 back-to-back meetings, a board meeting to prepare for with investors who have sky-high expectations, 6 new hires to onboard and 16 more to find, and–not least–a product to improve for the customers we are trying to serve and retain–only to wake up, rinse (maybe) and repeat tomorrow?? (We didn't even mention the chat and email messages mounting in the background.) How could I possibly exit "busy anxiousness" and practice calm centeredness amidst this chaos? (Notice what you feel just reading that–does your body tighten a bit?) Calm sounds nice–for vacation! I want results. There is a way, not to perfection and a stress-less existence, but rather a way of working, being, and leading from a deeper calm that creates enough space to harness the remaining (necessary) stress as fuel towards your goals. We call this way Rooted Stillness. We see Rooted Stillness as the key ingredient in the shift from Actor to Author. Why might be it be especially relevant to you right now? If your startup is growing rapidly, you're hitting (or already past) a key inflection point: expanding your focus from building a product/service to building a team and organization. It is in this formative moment that leadership is so crucial, when weaknesses–and strengths–as a leader become apparent and embed themselves as norms across the developing org.</p>
    <span class="play" style="left:292px;top:268px;width:20px;height:20px;background:#2a9ce0"></span>
  </div>

</div>
</body>
</html>
```